Harbor Sushi & Steak Dinner Menu

I'm looking for a MENU design with a particular feel. I want to have a base template made that I can then use for future alterations to the menu; ie I can go in and change out different entrees as the menu changes but the template will remain the same. (Ideally it would be in an Apple Pages format.). Also ideally - dinner menu will occupy 2 pages 8.5 x 11. The restaurant's name is Harbor. It is a MODERN steak house that will also feature Sushi, a Raw Bar, Exquisite Cocktails and a sophisticated nightlife crowd. I have attached our LOGO, a secondary logo that we will be featuring throughout the project including on the menu cover (the gold U). Finally - I have attached the content that we would like to see. AGAIN - I REITERATE: High end dining and lounge atmosphere. A couple of restaurants / menus that I love are Corvellin in NYC and Marrowby Steakhouse in Long Island NY. Please do not duplicate - just trying to offer some suggestions.

Requirements
Must have
• A sophisticated and elegant feel without being stuffy or old.

```html
<!DOCTYPE html>
<html lang="en">
<head>
<meta charset="utf-8">
<title>Harbor Sushi &amp; Steak — Dinner Menu</title>
<link href="https://fonts.googleapis.com/css2?family=Raleway:wght@300;400;500&family=Source+Sans+3:ital,wght@0,400;1,400&display=swap" rel="stylesheet">
<style>
  :root{
    --canvas:#ffffff;
    --page:#0a0a0a;
    --red:#e01f35;
    --gold:#d8ae4c;
    --ink:#f4f1ea;
    --head:'Raleway', sans-serif;
    --body:'Source Sans 3', sans-serif;
  }
  *{box-sizing:border-box;margin:0;padding:0}
  html,body{width:1200px;height:772px;overflow:hidden;background:var(--canvas)}
  .spread{position:relative;width:1200px;height:772px}
  .page{position:absolute;top:11px;width:577px;height:751px;background:var(--page);overflow:hidden}
  .page--left{left:14px}
  .page--right{left:611px}
  .frame{position:absolute;inset:0;width:577px;height:751px}
  .section{position:absolute;color:var(--ink);font-family:var(--body)}
  .section h2{font:300 14.5px/1 var(--head);color:var(--red);letter-spacing:.6px;text-transform:uppercase}
  .rule{height:4px;border-top:1px solid var(--gold);border-bottom:1px solid var(--gold);margin:6px 0 9px;opacity:.85}
  .plain li{list-style:none;font-size:10.5px;line-height:16px}
  .item{margin-bottom:8px}
  .item .name{display:block;color:var(--gold);font-size:10.5px;line-height:12px}
  .item .desc{display:block;font-style:italic;font-size:7.6px;line-height:9px}
  .col-l{left:30px;width:244px}
  .col-r{left:310px;width:244px}
  .rcol-l{left:26px;width:262px}
  .rcol-r{left:302px;width:246px}
  .sides{display:flex;gap:16px}
  .sides ul:first-child{width:178px}
  .sides .wrap{line-height:12px;margin:2px 0 3px}
  .brand{position:absolute;left:0;right:0;top:680px;text-align:center;
    font:500 30px/1 var(--head);color:var(--gold);letter-spacing:4px}
</style>
</head>
<body>
<div class="spread">

  <section class="page page--left">
    <svg class="frame" viewBox="0 0 577 751" aria-hidden="true">
      <path d="M12 10 H565 V672 L288.5 623 L12 672 Z" fill="none" stroke="var(--red)" stroke-width="1.6"/>
      <path d="M17 15 H560 V666 L288.5 617 L17 666 Z" fill="none" stroke="var(--red)" stroke-width="1.2"/>
    </svg>

    <div class="section col-l" style="top:35px">
      <h2>Sushi / Sashimi</h2><div class="rule"></div>
      <ul class="plain">
        <li>Toro; Blue Fin Tuna Belly (Gf)</li>
        <li>Unagi; Fresh Water Eel (Gf)</li>
        <li>Ebi; Cooked Shrimp (Gf)</li>
        <li>Sake; Salmon (Gf)</li>
        <li>Hamachi; Yellowtail (Gf)</li>
        <li>Madai; Red Snapper (Gf)</li>
        <li>Uni; Sea Urchin (Gf)</li>
        <li>Maguro; Tuna (Gf)</li>
        <li>Hirame; Fluke (Gf)</li>
      </ul>
    </div>

    <div class="section col-l" style="top:245px">
      <h2>Sushi Platters</h2><div class="rule"></div>
      <div class="item"><span class="name">Small</span><span class="desc">Five Pieces assorted sushi, nine pieces sashimi, spicy tuna roll (gf)</span></div>
      <div class="item"><span class="name">Large</span><span class="desc">Eight Pieces assorted sushi, eighteen pieces of sashimi, alaskan roll, rainbow roll (gf)</span></div>
    </div>

    <div class="section col-l" style="top:380px">
      <h2>Classic Rolls</h2><div class="rule"></div>
      <div class="item"><span class="name">Yellowtail</span><span class="desc">inside out roll with scallions (gf), Spicy Tuna or Salmon or Yellowtail, spicy mayo</span></div>
      <div class="item"><span class="name">California</span><span class="desc">crab meat, cucumber and avocado (gf)</span></div>
      <div class="item"><span class="name">Vegetable</span><span class="desc">avocado, cucumber, asparagus and pickled reddish (gf)</span></div>
      <div class="item"><span class="name">Spider</span><span class="desc">soft shell crab and avocado with eel sauce</span></div>
      <div class="item"><span class="name">Shrimp Tempura</span><span class="desc">deep fried tempura shrimp and eel sauce</span></div>
      <div class="item"><span class="name">Alaskan</span><span class="desc">salmon and avocado (gf)</span></div>
    </div>

    <div class="section col-r" style="top:35px">
      <h2>Special Rolls</h2><div class="rule"></div>
      <div class="item"><span class="name">The Harbor</span><span class="desc">tuna, salmon, yellowtail, avocado, spicy mayo, soy bean paper</span></div>
      <div class="item"><span class="name">King Crab Rainbow</span><span class="desc">king crab, avocado, cucumbers, assorted fish on top</span></div>
      <div class="item"><span class="name">Empress</span><span class="desc">Shrimp tempura, spicy tuna on top, eel sauce, spicy mayo</span></div>
      <div class="item"><span class="name">Spicy Girl</span><span class="desc">Spicy crunchy crab meat, cucumber, shrimp on top</span></div>
      <div class="item"><span class="name">Dragon</span><span class="desc">Eel, cucumber, avocado, and tobiko on top, eel sauce</span></div>
      <div class="item"><span class="name">Yummy</span><span class="desc">spicy crunchy salmon, avocado, mango and salmon on top</span></div>
      <div class="item"><span class="name">No. 9</span><span class="desc">Shrimp Tempura, avocado, kani, spicy mayo, tobiko</span></div>
      <div class="item"><span class="name">Sunrise Roll</span><span class="desc">spicy crunchy tuna and avocado, spicy crunchy salmon on top</span></div>
    </div>

    <div class="section col-r" style="top:333px">
      <h2>Seafood Raw Bar</h2><div class="rule"></div>
      <ul class="plain">
        <li>Lobster Cocktail</li>
        <li>Shrimp Cocktail</li>
        <li>Clams on the Half Shell</li>
        <li>Oysters on the Half Shell</li>
        <li>Colossal Crab Cocktail</li>
      </ul>
      <p style="font-size:10.5px;line-height:12px;margin-top:5px">Raw Bar Plate for One:</p>
      <p style="font-size:8px;line-height:10px">Two Shrimp, Half of a One Pound Lobster, Two Clams,<br>One East Coast Oyster, One West Coast Oyster</p>
    </div>

    <div class="section col-r" style="top:512px">
      <h2>Seafood Platters (gf)</h2><div class="rule"></div>
      <p style="font-size:8.5px;line-height:10px;margin-bottom:8px">Shrimp, Oysters, Clams, Lobster and Crab</p>
      <p style="font-size:10.5px">Large or Colossal</p>
    </div>

    <div class="brand">HARBOR</div>
  </section>

  <section class="page page--right">
    <svg class="frame" viewBox="0 0 577 751" aria-hidden="true">
      <path d="M12 10 H565 V672 L288.5 623 L12 672 Z" fill="none" stroke="var(--red)" stroke-width="1.6"/>
      <path d="M17 15 H560 V666 L288.5 617 L17 666 Z" fill="none" stroke="var(--red)" stroke-width="1.2"/>
    </svg>

    <div class="section rcol-l" style="top:28px">
      <h2>Appetizer</h2><div class="rule"></div>
      <div class="item"><span class="name">BAO Bun</span><span class="desc">hoisin bbq pancetta cut pork loin, crispy onions, micro mint</span></div>
      <div class="item"><span class="name">Five Spice Crispy Popcorn Crusted Prawns (2)</span><span class="desc">classic burre blanc</span></div>
      <div class="item"><span class="name">Jumbo Lump Crab</span><span class="desc">Citrus miso drizzle, spring pea puree, micro greens</span></div>
      <div class="item"><span class="name">Crispy Wonton Napoleon</span><span class="desc">cucumber gallete, ahi tuna, jumbo lump crab meat,<br>wasabi aioli, shoestring wontons</span></div>
      <div class="item"><span class="name">PEI Mussels</span><span class="desc">Charred artichoke hearts, blistered heirloom tomatoes, garlic white wine broth</span></div>
      <div class="item"><span class="name">New Zealand or Domestic Small Eye Lamb Chop (1)</span><span class="desc">crispy porcini risotto cake</span></div>
      <div class="item"><span class="name">Classic Wedge</span><span class="desc">bleu cheese, bacon lardons, heirloom tomatoes</span></div>
      <div class="item"><span class="name">Mixed Baby Greens</span><span class="desc">heirloom tomatoes, cucumber, red onion, dijon vinaigrette</span></div>
      <div class="item"><span class="name">Tabulleh</span><span class="desc">buckwheat grain, fresh mint, tomato concasse, cucumber, parsley, fresh squeezed lemon, EVOO., salt and pepper</span></div>
      <div class="item"><span class="name">Tomato Mozzarella Salad / Burratta</span></div>
      <div class="item"><span class="name">Spinach Salad</span><span class="desc">green apple, feta, currants, with per-simmons vinaigrette</span></div>
      <div class="item"><span class="name">Kale Caesar</span><span class="desc">homemade cacio e'peppe dressing, pecorino and parmesan cheese, toasted croutons</span></div>
    </div>

    <div class="section rcol-l" style="top:470px">
      <h2>Entrees</h2><div class="rule"></div>
      <div class="item"><span class="name">Pan Roasted Miso Glazed Black Cod</span><span class="desc">green tea noodle stir fry, Napa cabbage, carrot, Japanese eggplant</span></div>
      <div class="item"><span class="name">Pan Seared Striped Bass</span><span class="desc">lobster succotash in a tomato saffron broth</span></div>
      <div class="item"><span class="name">E.V.O.O. Salted / Grilled Swordfish</span><span class="desc">sun dried tomato, olive and caper tapenade, over basmati rice</span></div>
      <div class="item"><span class="name">Grilled Half Chicken</span><span class="desc">sun dried tomato and basil Israeli cous-cous, pan au jus</span></div>
    </div>

    <div class="section rcol-r" style="top:26px">
      <div class="item"><span class="name">Roasted Fresh Caviatelle Ratatoille</span><span class="desc">vegetable broth</span></div>
      <div class="item"><span class="name">Lobster Cartoccio</span><span class="desc">shrimp, mussels, clams, fresh herb tomato broth, tossed with bucatini</span></div>
      <div class="item"><span class="name">Charred Artichoke Hearts</span><span class="desc">heirloom tomatoes, caper berries, spring onions, fresh basil, white wine reduction over forbidden rice (gf)</span></div>
      <div class="item"><span class="name">Mediterranean Grilled Veggie Plate</span><span class="desc">artichoke hearts, Japanese eggplant, green &amp; white asparagus, seared heirloom tomatoes, roasted baby carrots, cauliflower rice, evoo &amp; fig drizzle (gf)</span></div>
    </div>

    <div class="section rcol-r" style="top:214px">
      <h2>USDA Prime Steaks (gf)</h2><div class="rule"></div>
      <ul class="plain">
        <li>10 Oz Filet</li>
        <li>14 or 16 oz New York Strip</li>
        <li>24 oz Boneless Ribeye</li>
        <li>36 oz Bone in Rib Eye</li>
        <li>Berkshire Pork Chop</li>
      </ul>
    </div>

    <div class="section rcol-r" style="top:348px">
      <h2>Sauces</h2><div class="rule"></div>
      <ul class="plain">
        <li>Cabernet Demi Glaz</li>
        <li>Gorganzola Brulle Cream</li>
        <li>Truffled Wild Mushroom Ragu</li>
        <li>Horseradish Cream</li>
        <li>House Steak Sauce</li>
      </ul>
    </div>

    <div class="section rcol-r" style="top:470px">
      <h2>Sides</h2><div class="rule"></div>
      <div class="sides">
        <ul class="plain">
          <li>Mashed Idaho Potatoes</li>
          <li class="wrap">Bacon, Sweet Corn, Caramelized Vidalia Onion fingerling potatoes</li>
          <li>Roasted Peanut Potatoes</li>
          <li>Creamed Spinach</li>
          <li>Sautéed Spinach</li>
          <li>Grilled Asparagus</li>
        </ul>
        <ul class="plain">
          <li>French Beans</li>
          <li>Israeli Cous Cous</li>
          <li class="wrap">Sweet Potato Steak Fries</li>
          <li>Corn Skillet</li>
        </ul>
      </div>
    </div>

    <div class="brand">HARBOR</div>
  </section>

</div>
</body>
</html>
```